Card Design for my dog training business Rustpaw Obedience

Need a business card design for my dog training business with my new logo. Want the card to come off professional yet fun. Want it to be very eye catchy as well. I normally have these at vet clinics, pet stores, and groomers. so need it to look better than my competitors.
Target Market(s)
dog owners
Industry/Entity Type
Dog Training
Contact Information for Business Card
needs logo, my name and info
Font styles to use
Serif
Colors
0255a3
ffffff
ec1f27
000000
333333
fbfbfb
Requirements
Must have
- Rustpaw Obedience
- Hollis Brandt
- 415 903 2267
- info@rustpawobedience.example
- www.rustpawobedience.example

```html
<!DOCTYPE html>
<html lang="en">
<head>
<meta charset="utf-8">
<title>Rustpaw Obedience – Business Card</title>
<link rel="stylesheet" href="https://fonts.googleapis.com/css2?family=Noto+Serif:wght@400;700&display=swap">
<style>
  :root {
    --stage: #e9e7e4;
    --ink: #000000;
    --text: #333333;
    --paper: #fbfbfb;
    --white: #ffffff;
    --silver-light: #d9d9d9;
    --silver-dark: #4a4a4a;
  }
  * { box-sizing: border-box; margin: 0; padding: 0; }
  html, body { width: 1200px; height: 900px; overflow: hidden; }
  body {
    background: var(--stage);
    font-family: "Noto Serif", Georgia, serif;
    position: relative;
  }
  .card {
    position: absolute;
    top: 298px;
    width: 530px;
    height: 303px;
    border-radius: 4px;
    overflow: hidden;
    box-shadow: 0 10px 28px rgba(0,0,0,0.22);
  }

  /* Front */
  .card--front { left: 50px; background: linear-gradient(160deg, #2a2a2a, var(--ink) 70%); }
  .front__artwork {
    position: absolute; left: 0; top: 0;
    width: 260px; height: 245px;
    background: radial-gradient(ellipse at 45% 55%, var(--silver-light) 0%, #8c8c8c 40%, var(--silver-dark) 70%, transparent 100%);
    opacity: 0.75;
  }
  .front__brand {
    position: absolute; left: 285px; top: 100px; width: 225px;
    color: var(--white); font-size: 28px; font-weight: 400;
    line-height: 1.15; text-align: center;
  }
  .front__web {
    position: absolute; right: 24px; bottom: 28px;
    color: var(--white); font-size: 14px;
  }
  .front__rule {
    position: absolute; left: 0; right: 0; bottom: 16px;
    height: 3px; background: var(--silver-light);
  }

  /* Back */
  .card--back { left: 620px; background: var(--paper); }
  .back__name {
    position: absolute; left: 30px; top: 32px;
    font-size: 22px; font-weight: 700; color: var(--ink);
  }
  .back__company {
    position: absolute; left: 30px; top: 64px;
    font-size: 14px; color: var(--text);
  }
  .back__rule-top {
    position: absolute; left: 30px; top: 88px; width: 290px;
    height: 1px; background: var(--ink);
  }
  .back__contacts { position: absolute; left: 30px; top: 100px; list-style: none; }
  .back__contacts li {
    display: flex; align-items: center; gap: 8px;
    font-size: 14px; color: var(--text); margin-bottom: 6px;
  }
  .back__contacts svg { width: 13px; height: 13px; fill: var(--ink); }
  .back__brand {
    position: absolute; right: 28px; top: 40px; width: 180px;
    display: flex; flex-direction: column; align-items: center; gap: 10px;
    font-size: 22px; color: var(--ink); line-height: 1.15; text-align: center;
  }
  .back__brand-mark { width: 44px; height: 44px; border-radius: 50%; background: var(--ink); }
  .back__rule-mid {
    position: absolute; left: 300px; top: 168px; width: 200px;
    height: 1px; background: var(--ink);
  }
  .back__tagline {
    position: absolute; right: 30px; top: 176px; width: 220px;
    font-size: 14px; color: var(--text); text-align: right; line-height: 1.35;
  }
  .back__band { position: absolute; left: 0; bottom: 0; width: 530px; height: 80px; }
  .back__web {
    position: absolute; right: 24px; bottom: 9px;
    color: var(--white); font-size: 15px;
  }
</style>
</head>
<body>
  <section class="card card--front" aria-label="Card front">
    <div class="front__artwork" role="img" aria-label="Silver foil illustration of two dogs"></div>
    <div class="front__brand">Rustpaw Obedience</div>
    <div class="front__web">www.rustpawobedience.example</div>
    <div class="front__rule"></div>
  </section>

  <section class="card card--back" aria-label="Card back">
    <h1 class="back__name">Hollis Brandt</h1>
    <p class="back__company">Rustpaw Obedience</p>
    <div class="back__rule-top"></div>
    <ul class="back__contacts">
      <li>
        <svg viewBox="0 0 24 24" aria-hidden="true"><path d="M6.6 10.8a15.1 15.1 0 0 0 6.6 6.6l2.2-2.2a1 1 0 0 1 1-.25 11.4 11.4 0 0 0 3.6.57 1 1 0 0 1 1 1V20a1 1 0 0 1-1 1A17 17 0 0 1 3 4a1 1 0 0 1 1-1h3.5a1 1 0 0 1 1 1c0 1.25.2 2.45.57 3.57a1 1 0 0 1-.25 1z"/></svg>
        415 903 2267
      </li>
      <li>
        <svg viewBox="0 0 24 24" aria-hidden="true"><path d="M2 5h20v14H2z M4 7v.5l8 5 8-5V7l-8 5z" fill-rule="evenodd"/></svg>
        info@rustpawobedience.example
      </li>
    </ul>
    <div class="back__brand"><span class="back__brand-mark"></span>Rustpaw Obedience</div>
    <div class="back__rule-mid"></div>
    <p class="back__tagline">“Training dogs across Texas one dog at a time.”</p>
    <svg class="back__band" viewBox="0 0 530 80" aria-hidden="true">
      <polygon points="0,0 190,0 190,3 0,3" fill="#000"/>
      <polygon points="0,12 196,12 226,44 530,44 530,80 0,80" fill="#000"/>
    </svg>
    <div class="back__web">www.rustpawobedience.example</div>
  </section>
</body>
</html>
```